Verantis Guest Event Collateral

Create a double-sided, oversized piece of collateral for a series of guest networking events that we'll be hosting in 2019

We are looking for this piece of collateral to be the size of an oversized post card (1/2 of an 8/5 x 11 piece of paper). The front should include the following: Verantis's Mission Statement: Continually foster a culture of community and education for focused business professionals. How do we do it? Using four distinct principles, Verantis offers business professionals the opportunity to be successful right now ,as well as next year. Through in-person meetings, virtual meetings, networking events, and educational opportunities Verantis offers members a chance to hit their goals not only this year, but every year! Collaboration: Work with like-minded, driven Verantis members to collaborate and overcome the objections, hurdles and challenges that all business professionals face, either in person at twice monthly meetings, or virtually, from the comfort of your home or office. Accountability: Stay on track, and complete the goals you have set for yourself! Weekly in person or virtual meetings afford all members the opportunity to review their plan twice a month with fellow Verantis members, and trained Verantis coaches. Referrals: In the midst of crafting an executable, measurable and attainable plan let Verantis build your business through a steady stream of referrals via six yearly networking events, specifically designed to ensure you walk away with new referral partners. Strategy: Let Verantis assist you in crafting a strategy within our proven business planning template; realistic, understandable, measurable, beyond normal, attainable and time bound. The back should include the following: Become a Verantis member for $150/month and join us for 6 Networking Events in 2019 plus much more! We aren’t just about collaboration, accountability and strategy! Creating opportunities for referrals is also a cornerstone of Verantis! To make certain we are delivering on this principle, Verantis will host 6 events throughout 2019, complete with specific activities at each event to ensure you meet everyone in the room, making immediate connects to build your referral network. Join now and put yourself in position for success in 2019! Name: Phone: Email: Company Name: Industry: Position: Credit Card Number: Exp. Date: Testimonials: Overall I think people are lazy. I know I am! The benefits I have found and have come to truly appreciate thru Verantis are a sense of professionalism, accountability and shared enthusiasm. These things break that cycle of laziness for me and, I am sure, many others. When I walk into a meeting I know that positive and helpful feedback is the name of the game. Feedback from others and in many other industries from my own has become a key and cornerstone to my business and personal success. I would urge anyone no matter what your occupation to attend a couple of meetings and see how this group of like minded professionals can help you to achieve more. More time, More success, More health, More security, More money, More happiness..............What could you use more of? Gordon T. Melby Sr. Automotive Consultant Ridgewater Leasing & Sales Thank you!

Target Market(s)

Small business owners, entrpreneurs, networkers, sales people

Industry/Entity Type

Business Consultant

Font styles to use
Sans Serif

Colors
f36f22
f68d4e
f8ba93
f78f20
faa54b

Requirements
Must have
• - Imagery
• - Our company logo
• - Clear CTA to check out our website (www.verantis-example.com)
• - Option to "Join the Verantis Community Today!" and include a spot for someone to fill in their name, email address, company name, and phone number
• - Reference that we host 6+ networking events in Denver throughout the year that are free to attend and are unlike any other networking event they've attended before
• - Mention that we have in-person meetings 2x per month, virtual meeting options, networking events, and educational events
• - Highlight the following acronym which references our core company components:
• Collaboration:
• Work with like-minded, driven Verantis members to collaborate and overcome the objections, hurdles and challenges that all business professionals face, in either in person twice monthly meetings, or virtually, from the comfort of your home of office.
• Accountability:
• Stay on track, and complete the goals you have set for yourself! Weekly in person or virtual meetings afford all members the opportunity to review their plan twice a month with your fellow Verantis members and trained Verantis coaches, to make certain you success is continuous throughout the year.
• Referrals:
• In the midst of crafting an executable, measurable and attainable plan let Verantis build your business through a steady stream of referral opportunities via twelve yearly networking events, specifically designed to ensure you walk away with new referral partners.
• Strategy:
• Let Verantis assist you in crafting a strategy within our proven business planning template; realistic, understandable, measurable, beyond normal, attainable and time bound.

```html
<!DOCTYPE html>
<html lang="en">
<head>
<meta charset="utf-8">
<title>Verantis Guest Event Collateral</title>
<link rel="stylesheet" href="https://fonts.googleapis.com/css2?family=Montserrat:wght@400;500;600;700&family=Open+Sans:wght@400;600&display=swap">
<style>
  :root{
    --orange:#f36f22;
    --orange-mid:#f68d4e;
    --orange-soft:#f8ba93;
    --amber:#f78f20;
    --amber-light:#faa54b;
    --ink:#222;
    --body:#3a3a3a;
    --panel:#ececec;
    --grey-circle:#a9a9a9;
    --band:#444;
    --stage:#e9e9e9;
    --white:#fff;
  }
  *{box-sizing:border-box;margin:0;padding:0}
  html,body{width:1200px;height:1200px;overflow:hidden;background:var(--stage)}
  body{position:relative;font-family:"Open Sans",Arial,sans-serif;color:var(--body)}
  .sheet{position:absolute;top:190px;width:540px;height:700px;background:var(--white);box-shadow:0 6px 18px rgba(0,0,0,.18);overflow:hidden}
  .sheet--front{left:40px}
  .sheet--back{left:620px}
  .side-label{position:absolute;top:920px;width:540px;text-align:center;font-family:"Montserrat",Arial,sans-serif;font-weight:700;font-size:30px;color:#555;letter-spacing:1px}
  .side-label--front{left:40px}
  .side-label--back{left:620px}

  /* Front */
  .hero{position:absolute;left:0;top:0;width:540px;height:440px;background:linear-gradient(160deg,#c9561a 0%,var(--orange) 45%,#a84410 100%)}
  .brand{position:absolute;display:flex;align-items:center;gap:8px;font-family:"Montserrat",Arial,sans-serif;font-weight:500;color:var(--white)}
  .brand__mark{display:inline-block;background:currentColor}
  .hero .brand{left:150px;top:58px;font-size:34px;letter-spacing:.5px}
  .hero .brand__mark{width:26px;height:26px}
  .hero__title{position:absolute;left:30px;right:30px;top:160px;text-align:center;font-family:"Montserrat",Arial,sans-serif;font-weight:600;font-size:46px;line-height:1.18;color:var(--white)}
  .hero__intro{position:absolute;left:40px;right:40px;top:320px;padding:14px 18px;text-align:center;font-family:"Montserrat",Arial,sans-serif;font-size:14.5px;line-height:1.4;color:var(--white);background:rgba(255,255,255,.12);border-top:1px solid rgba(255,255,255,.45);border-bottom:1px solid rgba(255,255,255,.45)}
  .provide__title{position:absolute;left:26px;top:464px;font-family:"Montserrat",Arial,sans-serif;font-weight:500;font-size:17px;color:var(--ink)}
  .provide__list{position:absolute;left:18px;right:18px;top:500px;display:flex;justify-content:space-between;list-style:none}
  .provide__item{min-width:100px;text-align:center}
  .provide__icon{display:block;margin:0 auto 10px;width:78px;height:78px}
  .provide__label{display:block;white-space:nowrap;font-family:"Montserrat",Arial,sans-serif;font-weight:600;font-size:12.5px;line-height:1.3;color:var(--orange)}
  .footer-band{position:absolute;left:0;width:100%;height:28px;background:var(--band);color:var(--white);text-align:center;font-family:"Montserrat",Arial,sans-serif;font-size:14px;line-height:28px;letter-spacing:4px}
  .sheet--front .footer-band{top:648px}

  /* Back */
  .back-photo{position:absolute;left:0;top:0;width:540px;height:205px;background:linear-gradient(135deg,#f3e4da 0%,#f6efe9 45%,#e8d3c6 100%)}
  .approach__title{position:absolute;left:22px;top:220px;font-family:"Montserrat",Arial,sans-serif;font-weight:500;font-size:17px;color:var(--ink)}
  .approach{position:absolute;left:0;top:252px;width:540px;height:225px;background:var(--panel);display:grid;grid-template-columns:1fr 1fr;gap:10px 18px;padding:12px 20px}
  .pillar{display:flex;gap:10px}
  .pillar__icon{flex:none;width:44px;height:44px;border-radius:50%;background:var(--orange-mid)}
  .pillar__name{font-family:"Montserrat",Arial,sans-serif;font-weight:500;font-size:12.5px;color:var(--orange);margin-bottom:3px}
  .pillar__text{font-size:8px;line-height:1.35;color:var(--body);text-align:justify}
  .form__title{position:absolute;left:22px;top:492px;font-family:"Montserrat",Arial,sans-serif;font-weight:500;font-size:13.5px;color:var(--orange)}
  .form{position:absolute;left:22px;right:22px;top:520px;display:flex;flex-direction:column;gap:9px}
  .form__field{height:19px;border:1px solid #888;border-radius:10px;padding-left:6px;font-size:10px;line-height:17px;color:var(--ink)}
  .sheet--back .brand{right:22px;top:628px;font-size:20px;color:#333}
  .sheet--back .brand__mark{width:15px;height:15px;background:var(--orange)}
  .sheet--back .footer-band{top:660px}
</style>
</head>
<body>

<section class="sheet sheet--front" aria-label="Front side">
  <div class="hero" role="img" aria-label="Audience at a networking event with raised hands, tinted orange">
    <div class="brand"><span class="brand__mark"></span>VERANTIS</div>
    <h1 class="hero__title">Join the Verantis Community Today!</h1>
    <p class="hero__intro">We host 6+ networking events in Denver throughout the year that are free to attend and are unlike any other networking event they've attended before</p>
  </div>

  <h2 class="provide__title">What we Provide</h2>
  <ul class="provide__list">
    <li class="provide__item">
      <svg class="provide__icon" viewBox="0 0 78 78" aria-hidden="true"><circle cx="39" cy="39" r="39" fill="#a9a9a9"/><g fill="none" stroke="#fff" stroke-width="2"><circle cx="28" cy="26" r="4"/><circle cx="50" cy="26" r="4"/><path d="M24 36h30M27 36v18M51 36v18M39 36v18"/></g></svg>
      <span class="provide__label">In-person meetings<br>2x per month</span>
    </li>
    <li class="provide__item">
      <svg class="provide__icon" viewBox="0 0 78 78" aria-hidden="true"><circle cx="39" cy="39" r="39" fill="#a9a9a9"/><g fill="none" stroke="#fff" stroke-width="2"><rect x="24" y="22" width="32" height="22" rx="2"/><circle cx="34" cy="48" r="4"/><path d="M26 60c0-5 4-8 8-8s8 3 8 8"/></g></svg>
      <span class="provide__label">Virtual meeting<br>options</span>
    </li>
    <li class="provide__item">
      <svg class="provide__icon" viewBox="0 0 78 78" aria-hidden="true"><circle cx="39" cy="39" r="39" fill="#a9a9a9"/><g fill="none" stroke="#fff" stroke-width="2"><circle cx="30" cy="26" r="4"/><circle cx="48" cy="26" r="4"/><circle cx="30" cy="44" r="4"/><circle cx="48" cy="44" r="4"/><path d="M23 36c0-4 3-5 7-5s7 1 7 5M41 36c0-4 3-5 7-5s7 1 7 5M23 54c0-4 3-5 7-5s7 1 7 5M41 54c0-4 3-5 7-5s7 1 7 5"/></g></svg>
      <span class="provide__label">Networking events</span>
    </li>
    <li class="provide__item">
      <svg class="provide__icon" viewBox="0 0 78 78" aria-hidden="true"><circle cx="39" cy="39" r="39" fill="#a9a9a9"/><g fill="none" stroke="#fff" stroke-width="2"><path d="M26 24l13-6 13 6-13 6z"/><circle cx="39" cy="36" r="7"/><path d="M25 60c0-8 6-12 14-12s14 4 14 12z"/></g></svg>
      <span class="provide__label">Educational<br>events</span>
    </li>
  </ul>

  <div class="footer-band">www.verantis-example.com</div>
</section>

<section class="sheet sheet--back" aria-label="Back side">
  <div class="back-photo" role="img" aria-label="Business plan document on a clipboard beside glasses and a calculator, soft warm tones"></div>

  <h2 class="approach__title">Verantis offers a four-pronged approach:</h2>
  <div class="approach">
    <div class="pillar">
      <span class="pillar__icon"></span>
      <div>
        <h3 class="pillar__name">Collaboration</h3>
        <p class="pillar__text">Work with like-minded, driven Verantis members to collaborate and overcome the objections, hurdles and challenges that all business professionals face, either in person twice monthly meetings, or virtually, from the comfort of your home of office.</p>
      </div>
    </div>
    <div class="pillar">
      <span class="pillar__icon"></span>
      <div>
        <h3 class="pillar__name">Accountability:</h3>
        <p class="pillar__text">Stay on track, and complete the goals you have set for yourself! Weekly in person or virtual meetings afford all members the opportunity to review their plan twice a month with your fellow Verantis members and trained Verantis coaches, to make certain you success is continuous throughout the year.</p>
      </div>
    </div>
    <div class="pillar">
      <span class="pillar__icon"></span>
      <div>
        <h3 class="pillar__name">Referrals:</h3>
        <p class="pillar__text">In the midst of crafting an executable, measurable and attainable plan let Verantis build your business through a steady stream of referral opportunities via twelve yearly networking events, specifically designed to ensure you walk away with new referral partners.</p>
      </div>
    </div>
    <div class="pillar">
      <span class="pillar__icon"></span>
      <div>
        <h3 class="pillar__name">Strategy:</h3>
        <p class="pillar__text">Let Verantis assist you in crafting a strategy within our proven business planning template; realistic, understandable, measurable, beyond normal, attainable and time bound.</p>
      </div>
    </div>
  </div>

  <h2 class="form__title">Fill up the following to be a part of VERANTIS</h2>
  <div class="form">
    <div class="form__field">Name:</div>
    <div class="form__field">Company name:</div>
    <div class="form__field">Email address:</div>
    <div class="form__field">Phone number:</div>
  </div>

  <div class="brand"><span class="brand__mark"></span>VERANTIS</div>
  <div class="footer-band">www.verantis-example.com</div>
</section>

<div class="side-label side-label--front">FRONT</div>
<div class="side-label side-label--back">BACK</div>

</body>
</html>
```